Packaging design for Virgin Coconut Oil. 100% pure cold pressed coconut oil

We need a new packaging and label design for our Virgin Coconut Oil product. It is currently marketed in the Philippines as a food supplement. We would like to try marketing it to other Asian countries such as Singapore, Malaysia and Hong Kong. The company has been producing this product since 2004 but now would like to venture into exporting our products overseas.

Would like to see designs with earth, natural "organic" colors. Fresh, Clean and pure look. Our trade mark is "Kestrel Meadow". Its a 100% pure cold pressed virgin coconut oil. All in all, we want to totally repackage our product and re-design the trademark to cater to export markets. Thanks!

Mid to High

Health Product

cadf82
9bcb3b
33b8a4
ffffff
3176b5
3276b5
0592cd
fbed22
fece3e

• Bottle shape design ideas.

```html
<!DOCTYPE html>
<html lang="en">
<head>
<meta charset="utf-8">
<title>Kestrel Meadow – Virgin Coconut Oil Label</title>
<link rel="stylesheet" href="https://fonts.googleapis.com/css2?family=Tinos:wght@400;700&display=swap">
<style>
  :root {
    --canvas-bg: #ffffff;
    --label-blue: #3176b5;
    --label-teal: #2fa99a;
    --label-lime: #cadf82;
  }
  html, body {
    margin: 0;
    padding: 0;
    width: 1200px;
    height: 1000px;
    overflow: hidden;
    background: var(--canvas-bg);
  }
  .canvas {
    position: relative;
    width: 1200px;
    height: 1000px;
    background: var(--canvas-bg);
  }
  .product-label {
    position: absolute;
    left: 427px;
    top: 271px;
    width: 345px;
    height: 458px;
  }
  .label-border { fill: var(--label-teal); }
  .label-body { fill: var(--label-blue); }
  .label-inner-rule { fill: none; stroke: var(--label-lime); stroke-width: 4; }
  .label-mark { fill: var(--label-lime); }
  .label-rule { stroke: var(--label-lime); stroke-width: 3; }
  .brand-name, .brand-sub, .product-type, .rating-stars {
    fill: var(--label-lime);
    font-family: "Tinos", "Times New Roman", serif;
    font-weight: 400;
  }
  .brand-name { font-size: 50px; }
  .brand-sub { font-size: 29px; letter-spacing: 6px; }
  .rating-stars { font-size: 19px; letter-spacing: 2px; }
  .product-type { font-size: 21px; font-weight: 700; letter-spacing: 0.5px; }
</style>
</head>
<body>
<main class="canvas">
  <svg class="product-label" viewBox="0 0 345 458" aria-label="Kestrel Meadow virgin coconut oil label">
    <defs>
      <path id="product-type-arc" d="M 40 300 A 132 124 0 0 0 305 300"/>
    </defs>
    <rect class="label-border" x="0" y="0" width="345" height="458" rx="172" ry="190"/>
    <rect class="label-body" x="7" y="7" width="331" height="444" rx="165" ry="183"/>
    <rect class="label-inner-rule" x="19" y="19" width="307" height="420" rx="153" ry="171"/>

    <circle class="label-mark" cx="172" cy="90" r="18"/>

    <text class="brand-name" x="172.5" y="220" text-anchor="middle">KESTREL</text>
    <text class="brand-sub" x="175" y="268" text-anchor="middle">MEADOW</text>

    <line class="label-rule" x1="45" y1="287" x2="300" y2="287"/>
    <text class="rating-stars" x="173" y="317" text-anchor="middle">★★★★★</text>
    <line class="label-rule" x1="85" y1="333" x2="260" y2="333"/>

    <circle class="label-mark" cx="51" cy="322" r="3"/>
    <circle class="label-mark" cx="294" cy="322" r="3"/>
    <text class="product-type">
      <textPath href="#product-type-arc" startOffset="50%" text-anchor="middle">VIRGIN COCONUT OIL</textPath>
    </text>
  </svg>
</main>
</body>
</html>
```